Specialist Medical practice after professional trifold flyer design for patient information brochure

I am the Director of the Hollowbrook Clinic, a specialist medial and surgical practice in Australia. I am after a professional design of a patient information trifold flyer that can be used for web distribution or for commercial printing for upcoming educational event. The design would need to allow change of images and text to be used as template for future topics but have a common brand look across them. Colours would follow the logo, but primarily blue colours for the hollowbrook theme. The inside text needs to be clearly contrasted to the background for easy reading, as often elderly patients. The design would make use of curves or circles, but open for hexagonal, triangle square vector components. I have included an outline for the initial brochure and included images to include. Other stock background images can be used if they increase the impact of the design over included. A winning design is also one that could be modified to a 4 page bi-fold brochure

Target Market(s)

This will be provided to patients in GP practices, podiatry clinics, radiological practices. Aimed at patients to read and be compelled to look to site or get consultation with me

Industry/Entity Type

Medical

Font styles to use
Serif
Sans Serif

Colors
33a6d7
0355a3
86cfc6
cedeed
0292cd
85cae6

Requirements
Must have
• The front cover needs to engage the patient to pick up and read- yes I have a painful ankle and want to find out more. the goal for the inside is to provide the options but be able to direct to website for more info - website currently undergoing upgrade. After professional modern look. Not bright contrasting colours like many advertising brochures. Needs to able to have images and text changed but following same look to create new topics
Nice to have
• The focus is a Tri-fold brochure. Nice to be able to modify to bifold. A winning design would even offer both, or submit separate bifold and trifold. I am open to different versions of similar look. (eg option of brochure with curved elements, triangular or square, or hexagonal.
Should not have
• To many contrasting colours. Text must be easily read on background, either white or coloured background texture with transparency

```html
<!DOCTYPE html>
<html lang="en">
<head>
<meta charset="utf-8">
<title>Hollowbrook Clinic – Ankle Arthritis Brochure</title>
<link href="https://fonts.googleapis.com/css2?family=Open+Sans:wght@400;600&display=swap" rel="stylesheet">
<style>
  :root {
    --brand-blue: #2a93bf;
    --brand-deep: #0292cd;
    --heading-blue: #1c8fc2;
    --link-blue: #0a6ea8;
    --ink: #4a4f55;
    --paper: #ffffff;
    --stage: #7c8288;
    --slate-dark: #2d3740;
    --slate-mid: #4a5a66;
    --xray-glow: #85cae6;
  }
  * { box-sizing: border-box; margin: 0; padding: 0; }
  html, body { width: 1200px; height: 777px; overflow: hidden; }
  body {
    background: var(--stage);
    font-family: "Open Sans", Arial, sans-serif;
    color: var(--ink);
  }
  .brochure {
    display: flex;
    width: 1200px;
    height: 777px;
  }
  .panel {
    position: relative;
    width: 400px;
    height: 777px;
    overflow: hidden;
    background: var(--paper);
  }
  .panel + .panel { border-left: 1px solid #e3e7ea; }

  /* Left flap */
  .panel--decision { background: var(--slate-dark); }
  .decision-backdrop { position: absolute; inset: 0; }
  .decision-copy {
    position: relative;
    padding: 40px 36px 0 40px;
    color: #fff;
    font-size: 12.5px;
    line-height: 1.5;
  }
  .decision-copy p + p { margin-top: 12px; }
  .decision-copy .section-title { color: #fff; }
  .photo-consult {
    position: absolute;
    left: 196px; top: 372px;
    width: 150px; height: 150px;
    border-radius: 50%;
    border: 5px solid var(--brand-blue);
    background: radial-gradient(circle at 40% 35%, #f4f7f9, #c9d6df 60%, #7d93a3);
  }
  .illustration-foot {
    position: absolute;
    left: 0; top: 520px;
    width: 400px; height: 257px;
    background: radial-gradient(ellipse at 55% 70%, rgba(133,202,230,.45), rgba(74,90,102,.2) 55%, transparent 75%);
  }
  .quote {
    position: absolute;
    left: 212px; top: 590px;
    width: 170px;
    color: #fff;
    font-size: 13px;
    line-height: 1.35;
  }

  /* Inner panels */
  .content { padding: 34px 34px 0 38px; font-size: 12.5px; line-height: 1.5; }
  .content p { margin-bottom: 10px; }
  .section-title {
    display: flex; align-items: center; gap: 7px;
    font-size: 15px; font-weight: 400;
    letter-spacing: .3px; text-transform: uppercase;
    color: var(--heading-blue);
    margin-bottom: 8px;
  }
  .section-title svg { flex: none; }
  .section + .section { margin-top: 22px; }
  .xray {
    float: right;
    width: 150px; height: 150px;
    margin: 6px 0 6px 12px;
    border-radius: 50%;
    shape-outside: circle(50%);
    border: 5px solid var(--brand-deep);
    background: radial-gradient(circle at 45% 45%, #d9dde0, #8a9096 45%, #2b2f33 80%);
  }
  .web-link { color: var(--link-blue); font-weight: 600; }
</style>
</head>
<body>
<main class="brochure">

  <section class="panel panel--decision">
    <svg class="decision-backdrop" width="400" height="777" viewBox="0 0 400 777" aria-hidden="true">
      <defs>
        <linearGradient id="slateFade" x1="0" y1="0" x2="0" y2="1">
          <stop offset="0" stop-color="#5a6a76"/>
          <stop offset="1" stop-color="#2d3740"/>
        </linearGradient>
      </defs>
      <rect width="400" height="777" fill="url(#slateFade)"/>
      <path d="M0 0 H400 V420 C330 470 250 470 170 455 C100 442 40 445 0 470 Z" fill="#2a93bf"/>
      <g fill="none" stroke="#cde6f2" stroke-opacity=".7">
        <circle cx="120" cy="650" r="12" stroke-width="3"/>
        <circle cx="120" cy="650" r="24" stroke-width="2"/>
        <circle cx="120" cy="650" r="38" stroke-width="1.5" stroke-opacity=".4"/>
      </g>
    </svg>
    <div class="decision-copy">
      <h2 class="section-title">
        <svg width="11" height="11" viewBox="0 0 11 11"><path d="M4 0h3v4h4v3H7v4H4V7H0V4h4z" fill="#fff"/></svg>
        Make a informed decision
      </h2>
      <p>When pain medication, activity modification and shoe ware modification is no longer effective to control the pain then then it is worthwhile discussing with your GP for referral to Dr Martin Hale for an opinion on further treatment. As an Orthopaedic Foot and Ankle surgeon, he will be able to assess your conditions and give advice on the best options for your treatment.</p>
      <p>The decision on the best option is based on your age, activity level, existing medical problems, previous ankle treatment and your expected outcome from treatment. In the situation of end stage arthritis options consist of either Ankle fusion or Total Ankle replacement.</p>
    </div>
    <div class="photo-consult" role="img" aria-label="Photo of a doctor's desk with a stethoscope and a hand writing notes"></div>
    <div class="illustration-foot" role="img" aria-label="X-ray style illustration of a foot and ankle with a highlighted pain point"></div>
    <p class="quote">“Dr Martin Hale can give you advice on the best options for your treatment.”</p>
  </section>

  <section class="panel panel--conditions">
    <div class="content">
      <article class="section">
        <h2 class="section-title">
          <svg width="11" height="11" viewBox="0 0 11 11"><path d="M4 0h3v4h4v3H7v4H4V7H0V4h4z" fill="#1c8fc2"/></svg>
          Ankle arthritis
        </h2>
        <p>Ankle arthritis is a painful condition where there is loss of cartilage from the ankle joint surface. Although not as common as knee or hip arthritis, pain can be debilitating affecting quality of life.</p>
        <div class="xray" role="img" aria-label="X-ray of an arthritic ankle joint"></div>
        <p>Arthritis of the joint can be caused by trauma such as fracture or recurrent instability or secondary from inflammatory conditions such as rheumatoid arthritis.</p>
        <p>Pain from the joint will occur with activity causing a limp, limiting walking speed and distance. Often there is swelling of the joint with progressive loss of motion.</p>
        <p>Diagnosis is made with examination of the ankle and weight bearing x-rays showing loss of joint space.</p>
      </article>
      <article class="section">
        <h2 class="section-title">
          <svg width="11" height="11" viewBox="0 0 11 11"><path d="M4 0h3v4h4v3H7v4H4V7H0V4h4z" fill="#1c8fc2"/></svg>
          Ankle fusion surgery
        </h2>
        <div class="xray" role="img" aria-label="X-ray of an ankle fused with a plate and screws"></div>
        <p>This operation aims to stiffen the ankle joint by fusing the tibia and talus together in the optimal position for function. The common thought is that there will be no movement of the foot, and the patient will walk with a limp. The fusion only occurs at the ankle joint, leaving motion available to the surrounding joints. Although there is decreased motion, you will walk more normally after a fusion without a limp as the pain to the joint is removed.</p>
        <p>For more information on ankle fusion, risks and recovery visit our website:<br><span class="web-link">www.hollowbrookclinic.com.au/Ankle-Fusion</span></p>
      </article>
    </div>
  </section>

  <section class="panel panel--treatment">
    <div class="content">
      <article class="section">
        <h2 class="section-title">
          <svg width="11" height="11" viewBox="0 0 11 11"><path d="M4 0h3v4h4v3H7v4H4V7H0V4h4z" fill="#1c8fc2"/></svg>
          Total ankle replacement surgery
        </h2>
        <div class="xray" role="img" aria-label="X-ray of a total ankle replacement implant"></div>
        <p>In suitable patients there may be the option to maintain joint motion and perform a Total Ankle Replacement. Like a hip or knee replacement operation, the arthritic joint is removed and replaced with an artificial joint. Like an ankle fusion there will alleviation of the pain and limp with maintenance of the ankle joint motion. Recovery to walking post-surgery is often much sooner than with ankle fusion. Dr Martin Hale is one of the few surgeons to have completed an international fellowship in ankle replacement surgery and has been performing the technique since 2008. He is currently performing the technique using the Meridian Total ankle with Compass guides.</p>
        <p>For more information on ankle fusion, risks and recovery visit our website:<br><span class="web-link">www.hollowbrookclinic.com.au/Ankle-Replacement</span></p>
      </article>
      <article class="section">
        <h2 class="section-title">
          <svg width="11" height="11" viewBox="0 0 11 11"><path d="M4 0h3v4h4v3H7v4H4V7H0V4h4z" fill="#1c8fc2"/></svg>
          Results of surgery
        </h2>
        <p>Successful surgery in the suitable patient will help resolve the pain associated with the ankle arthritis. Ankle Fusion surgery is ideal for patients with heavy labour work, allowing them to return to previous activities. There may be the risk of arthritis to surrounding joints in the future, but often this occurs many years down the track. Results from Total Ankle replacement surgery have been improving over the years, but there is known risks of loosening, cyst formation or failure of the joint over time that can occur in some patients. It is important to have a opinion from an Orthopaedic Foot and Ankle Surgeon experienced in the these procedure to determine which procedure will provide the best long term solution for you.</p>
      </article>
    </div>
  </section>

</main>
</body>
</html>
```